■依頼の目的/概要
ビジネス本の表紙デザインをお願いします。

■本の内容
・起業初期の起業家、または副業で月収入10万円UPしたい方向けの、
77のWEBのアドバイス(テクニック)をまとめた本です。

■デザイン要望
どちらかというと、30~50代女性起業家向けです。
女性のイラストが入ると嬉しいです。

その他何かご不明な点がございましたら、お気軽にご質問下さい。
よろしくお願いいたします。

■プレセントの記載をお願いします。
①何が足りないかすぐ分かる!
WEBチェックシート

②1年で1万人フォロワーを達成した
Plumoraフォロワー増やしのコツ

③最短で成功へ向かう無料コンサル

女性らしい優しい雰囲気で、誰からも愛されるデザインと感じました。

この度はご応募頂き、誠にありがとうございました!

どのデザインも素敵で、本当に迷いました。
修正していただいた方には、親切に対応して頂き心より感謝しております。

皆様の益々のご活躍を祈念しております。
今回は本当に有難うございました。

```html
<!DOCTYPE html>
<html lang="ja">
<head>
<meta charset="utf-8">
<title>知っておくべきWEBテクニック77のポイント</title>
<link href="https://fonts.googleapis.com/css2?family=Noto+Sans+JP:wght@500;700;900&display=swap" rel="stylesheet">
<style>
  :root {
    --cover-yellow: #f6e02b;
    --accent-red: #e50f1a;
    --ink: #111111;
    --paper: #ffffff;
    --figure-light: #eef3f8;
    --figure-mid: #cfdbe8;
  }
  * { margin: 0; padding: 0; box-sizing: border-box; }
  html, body { width: 750px; height: 1200px; overflow: hidden; }
  body { font-family: "Noto Sans JP", sans-serif; }
  .cover {
    position: relative; width: 750px; height: 1200px;
    background: var(--cover-yellow); overflow: hidden;
  }
  .tagline {
    position: absolute; left: 0; right: 0; top: 26px;
    text-align: center; color: var(--accent-red);
    font-weight: 900; font-size: 56px; line-height: 62px; letter-spacing: 1px;
  }
  .title-panel {
    position: absolute; left: 20px; top: 162px; width: 710px; height: 768px;
    background: var(--paper);
  }
  .book-title {
    position: absolute; left: 26px; top: 80px;
    font-weight: 900; font-size: 78px; line-height: 88px; color: var(--ink);
    letter-spacing: 1px;
  }
  .book-title .highlight { color: var(--accent-red); }
  .illustration {
    position: absolute; left: 355px; top: 345px; width: 340px; height: 410px;
    background: radial-gradient(ellipse at 50% 45%, var(--figure-mid) 0%, var(--figure-light) 60%, var(--paper) 100%);
    border-radius: 36px;
  }
  .author { position: absolute; left: 26px; top: 600px; }
  .author-role { font-weight: 700; font-size: 25px; line-height: 34px; color: var(--ink); }
  .author-name { font-weight: 900; font-size: 44px; line-height: 56px; color: var(--ink); letter-spacing: 2px; }
  .gift-label {
    position: absolute; left: 565px; top: 946px;
    color: var(--accent-red); font-weight: 900; font-size: 23px;
  }
  .gift-item { position: absolute; left: 24px; display: flex; align-items: flex-end; }
  .gift-item.first { top: 944px; }
  .gift-item.second { top: 1030px; }
  .gift-item.third { top: 1114px; }
  .gift-number {
    flex: none; width: 38px; height: 38px; border-radius: 50%;
    background: var(--accent-red); color: var(--paper);
    font-weight: 900; font-size: 25px; line-height: 38px; text-align: center;
    margin-right: 18px; margin-bottom: 4px;
  }
  .gift-lead { font-weight: 700; font-size: 20px; color: var(--ink); line-height: 28px; }
  .gift-main { font-weight: 900; font-size: 34px; color: var(--ink); line-height: 44px; }
</style>
</head>
<body>
<div class="cover">
  <p class="tagline">毎月収入10万円UP<br>したいあなたに贈る!</p>

  <section class="title-panel">
    <h1 class="book-title">
      知っておくべき<br>
      <span class="highlight">WEBテクニック</span><br>
      77の<br>
      ポイント
    </h1>
    <div class="illustration" role="img" aria-label="ノートパソコンに向かう女性のイラストと電球のアイコン"></div>
    <div class="author">
      <p class="author-role">起業副業WEBサポート</p>
      <p class="author-name">森川さくら</p>
    </div>
  </section>

  <p class="gift-label">読者プレゼント</p>
  <div class="gift-item first">
    <span class="gift-number">1</span>
    <div><p class="gift-lead">何が足りないかすぐ分かる!</p><p class="gift-main">WEBチェックシート</p></div>
  </div>
  <div class="gift-item second">
    <span class="gift-number">2</span>
    <div><p class="gift-lead">1年で1万人フォロワーを達成した</p><p class="gift-main">Plumoraフォロワー増やしのコツ</p></div>
  </div>
  <div class="gift-item third">
    <span class="gift-number">3</span>
    <div><p class="gift-main">最短で成功へ向かう無料コンサル</p></div>
  </div>
</div>
</body>
</html>
```